Business Card Design Project

Refresh of logo attached. Require text underneath to be more ledgible, crisper & cleaner.

Overall, staying with same colour scheme need a brighter, crisper, easily readible business card style.

Industry/Entity Type

Business

```html
<!DOCTYPE html>
<html lang="en">
<head>
<meta charset="utf-8">
<title>Orvela Business Card</title>
<link rel="stylesheet" href="https://fonts.googleapis.com/css2?family=Arimo:wght@400;700&family=Questrial&display=swap">
<style>
  :root {
    --page-bg: #ecebe8;
    --card-bg: #ffffff;
    --ink: #231f20;
    --navy: #27394a;
    --steel: #436c8a;
    --steel-deep: #37607e;
    --white: #ffffff;
  }
  html, body {
    margin: 0;
    width: 1200px;
    height: 1000px;
    overflow: hidden;
    background: var(--page-bg);
  }
  .card {
    position: absolute;
    left: 60px;
    top: 208px;
    width: 1080px;
    height: 584px;
    background: var(--card-bg);
    box-shadow: 0 6px 18px rgba(0,0,0,0.18);
    font-family: "Arimo", Arial, sans-serif;
    color: var(--ink);
    overflow: hidden;
  }
  .brand {
    position: absolute;
    left: 50px;
    top: 62px;
    display: flex;
    align-items: center;
    gap: 26px;
  }
  .brand-mark {
    width: 72px;
    height: 72px;
    background: var(--navy);
  }
  .brand-name {
    font-family: "Arimo", Arial, sans-serif;
    font-weight: 400;
    font-size: 98px;
    line-height: 1;
    letter-spacing: 2px;
    color: var(--ink);
  }
  .brand-tagline {
    position: absolute;
    right: 541px;
    top: 176px;
    text-align: right;
    line-height: 1.3;
  }
  .tagline-lead {
    display: block;
    font-size: 22px;
    color: var(--ink);
  }
  .tagline-title {
    display: block;
    font-size: 22px;
    letter-spacing: 1.5px;
    word-spacing: 6px;
    color: var(--steel);
  }
  .contact {
    position: absolute;
    right: 53px;
    top: 310px;
    text-align: right;
  }
  .contact-name {
    font-weight: 700;
    font-size: 45px;
    word-spacing: 22px;
    margin: 0;
    line-height: 1.1;
  }
  .contact-role {
    font-family: "Questrial", Arial, sans-serif;
    font-size: 34px;
    word-spacing: 14px;
    letter-spacing: 0.5px;
    margin: 6px 0 0;
  }
  .contact-phones {
    display: flex;
    justify-content: space-between;
    font-size: 25px;
    margin-top: 14px;
  }
  .contact-email {
    font-size: 23px;
    margin-top: 6px;
  }
  .footer-band {
    position: absolute;
    left: 0;
    bottom: 0;
    width: 100%;
    height: 54px;
    display: flex;
  }
  .footer-site {
    width: 427px;
    background: var(--navy);
    color: var(--white);
    font-size: 31px;
    letter-spacing: 1.5px;
    display: flex;
    align-items: center;
    justify-content: center;
  }
  .footer-divider {
    width: 4px;
    background: var(--white);
  }
  .footer-accent {
    flex: 1;
    background: linear-gradient(90deg, var(--steel) 0%, var(--steel-deep) 100%);
  }
</style>
</head>
<body>
  <article class="card">
    <div class="brand">
      <div class="brand-mark"></div>
      <div class="brand-name">ORVELA</div>
    </div>
    <div class="brand-tagline">
      <span class="tagline-lead">Ontario Registry of</span>
      <span class="tagline-title">CERTIFIED ESTATE ADVISORS</span>
    </div>
    <div class="contact">
      <h1 class="contact-name">Peter R. Lawson</h1>
      <p class="contact-role">Certified Executor Advisor</p>
      <div class="contact-phones">
        <span>T : (416) 555 0142</span>
        <span>M : (647)555 0187</span>
      </div>
      <div class="contact-email">peter@orvela.ca</div>
    </div>
    <div class="footer-band">
      <div class="footer-site">www.orvela.ca</div>
      <div class="footer-divider"></div>
      <div class="footer-accent"></div>
    </div>
  </article>
</body>
</html>
```